New south Australia high-end red wine label & logo design

Marvel Ridge Estate exports premium south Australian wine to oversea market. We are looking for a professional graphic designer to design a full set of wine label and logo for our new red wine, the label & logo should look 'high-end' & Luxury and attractive. Black & gold color is preferred. I have attached example images to demonstrate the feel that we are looking for. These are just a possible starting point. The expectation is that the label would be professional/polished. I am open to any and all designs that would alter my perception of what will be best!

Target customer -

we need the label to be print-ready.

There will be 3 parts to this design.

Top Cover design with gold text wrapped, the front label and the back label

-Brand name Marvin Estate
-text wine of Australia
-text Cabernet
-Year 2015
-text Sourced from premium Australian wine growing region Kelmarsh valley

Look and Feel:
• Elegant
• Serious
• Modern/Traditional
• Professional
• Gender Neutral
• Upmarket

--------------Back Label text---------------
Rich and opulent with intense fruit aromas of black berry, liquorice and cassis with hints of dark chocolate and pungent spices. Sumptuous and textured palate with beautifully detailed ripe black fruits flowing seamlessly across the palate. French oak provides a complex harmony and finish of great length, balance and purity.

Produced by Kova Lindquist Holdings International Pty Ltd
27 Felbrook Lane,Norvale, South Australia, 5172
14.5 ALC/VOL
Wine of Australia
Approx 8.3 Standard Drinks
Contains Sulphites
750 ML
Please leave the space for Bar Code

Requirements
Must have
• wine name, wine logo, wine type etc (should include all 'must-have the required fields wine lable)
Nice to have
• Desginer's own idea
Should not have
• should not be too playful

```html
<!DOCTYPE html>
<html lang="en">
<head>
<meta charset="utf-8">
<title>Marvin Estate Cabernet – Front Label</title>
<link rel="stylesheet" href="https://fonts.googleapis.com/css2?family=Cinzel:wght@400;500&family=Cormorant+Garamond:wght@500&display=swap">
<style>
  :root {
    --backdrop: #2b2b2b;
    --label-black: #0f0f0f;
    --gold: #c9a13a;
    --gold-light: #e7c866;
    --gold-dark: #8a6a1c;
    --ivory: #e9e4d8;
    --wine-red: #c4161c;
  }
  * { margin: 0; padding: 0; box-sizing: border-box; }
  html, body {
    width: 718px;
    height: 1200px;
    overflow: hidden;
    background: var(--backdrop);
  }
  .canvas {
    position: relative;
    width: 718px;
    height: 1200px;
  }
  .front-label {
    position: absolute;
    left: 79px;
    top: 259px;
    width: 560px;
    height: 682px;
    background: var(--label-black);
    text-align: center;
    color: var(--ivory);
  }
  .crest-art {
    position: absolute;
    left: 151px;
    top: 38px;
    width: 258px;
    height: 262px;
    border-radius: 6px;
    background: radial-gradient(ellipse at 50% 45%, var(--gold-light) 0%, var(--gold) 45%, var(--gold-dark) 100%);
    opacity: 0.85;
  }
  .vintage {
    position: absolute;
    left: 0;
    right: 0;
    top: 290px;
    font-family: "Cinzel", serif;
    font-size: 30px;
    letter-spacing: 4px;
    color: var(--ivory);
  }
  .brand-name {
    position: absolute;
    left: 0;
    right: 0;
    top: 408px;
    font-family: "Cormorant Garamond", serif;
    font-weight: 500;
    font-size: 66px;
    line-height: 1;
    color: var(--gold);
  }
  .varietal {
    position: absolute;
    left: 0;
    right: 0;
    top: 484px;
    display: flex;
    align-items: center;
    justify-content: center;
    gap: 16px;
    font-family: "Cinzel", serif;
    font-size: 13px;
    letter-spacing: 10px;
    color: var(--ivory);
  }
  .varietal::before,
  .varietal::after {
    content: "";
    width: 42px;
    height: 1px;
    background: var(--ivory);
    opacity: 0.8;
  }
  .brand-square {
    position: absolute;
    left: 251px;
    top: 521px;
    width: 58px;
    height: 58px;
    border: 3px solid var(--wine-red);
  }
  .region-note {
    position: absolute;
    left: 0;
    right: 0;
    top: 596px;
    font-family: "Cinzel", serif;
    font-size: 8.5px;
    line-height: 13px;
    letter-spacing: 2.5px;
    color: var(--ivory);
  }
  .region-name {
    position: absolute;
    left: 0;
    right: 0;
    top: 640px;
    font-family: "Cinzel", serif;
    font-size: 22px;
    letter-spacing: 1.5px;
    color: var(--ivory);
  }
</style>
</head>
<body>
  <main class="canvas">
    <section class="front-label">
      <div class="crest-art" role="img" aria-label="Gold foil illustration of a rampant winged griffin"></div>
      <p class="vintage">2015</p>
      <h1 class="brand-name">Marvin Estate</h1>
      <p class="varietal">CABERNET</p>
      <div class="brand-square"></div>
      <p class="region-note">SOURCED FROM<br>PREMIUM AUSTRALIAN<br>WINE GROWING REGION</p>
      <p class="region-name">KELMARSH VALLEY</p>
    </section>
  </main>
</body>
</html>
```